Name card design for Southeast Asian Crowdfunding Startup

We need a double paged design for our company name cards.

We are a Singapore based crowd funding startup looking to operate regionally in Southeast Asia. Our service will be to match-make borrowers and lenders for loans, equity, property etc.

We have a logo already designed and hope for that to be used in the name card.

Industry/Entity Type

It Company

```html
<!DOCTYPE html>
<html lang="en">
<head>
<meta charset="utf-8">
<title>Meridian Lending Circle – Name Card</title>
<link rel="stylesheet" href="https://fonts.googleapis.com/css2?family=Ubuntu:wght@400;500;700&display=swap">
<style>
  :root {
    --backdrop: #e8ecef;
    --card: #f7f7f6;
    --ink: #3a3a3c;
    --ink-soft: #4a4a4d;
    --accent: #e9a02b;
    --brand-pink: #d6418a;
    --shadow: rgba(20, 40, 60, 0.14);
  }
  * { box-sizing: border-box; margin: 0; padding: 0; }
  html, body {
    width: 1200px;
    height: 900px;
    overflow: hidden;
    background: var(--backdrop);
    font-family: "Ubuntu", Arial, sans-serif;
    color: var(--ink);
  }
  .sheet {
    width: 1200px;
    height: 900px;
    display: flex;
    flex-direction: column;
    align-items: center;
    justify-content: center;
    gap: 48px;
  }
  .card {
    position: relative;
    width: 640px;
    height: 356px;
    background: var(--card);
    box-shadow: 0 10px 28px var(--shadow);
    overflow: hidden;
  }
  .card__band {
    position: absolute;
    left: 0; right: 0; bottom: 0;
    height: 16px;
    background: var(--accent);
  }

  /* Front side */
  .card--front .brand {
    position: absolute;
    left: 0; right: 0; top: 0; bottom: 16px;
    display: flex;
    flex-direction: column;
    align-items: center;
    justify-content: center;
    gap: 14px;
  }
  .brand__mark {
    display: flex;
    align-items: center;
    gap: 16px;
  }
  .brand__dot {
    width: 30px;
    height: 30px;
    border-radius: 50%;
    background: var(--brand-pink);
    flex: none;
  }
  .brand__name {
    font-size: 34px;
    font-weight: 400;
    letter-spacing: 0.04em;
    text-transform: uppercase;
    color: var(--ink);
  }
  .brand__web {
    font-size: 16px;
    color: var(--ink-soft);
    letter-spacing: 0.02em;
  }

  /* Back side */
  .card--back .person {
    position: absolute;
    left: 40px;
    top: 40px;
  }
  .person__name {
    font-size: 25px;
    font-weight: 400;
    letter-spacing: 0.02em;
  }
  .person__role {
    margin-top: 4px;
    font-size: 14px;
    letter-spacing: 0.08em;
    text-transform: uppercase;
    color: var(--ink-soft);
  }
  .contact {
    position: absolute;
    left: 40px;
    top: 150px;
    list-style: none;
    font-size: 16px;
  }
  .contact__item {
    display: flex;
    align-items: center;
    gap: 12px;
    height: 26px;
  }
  .contact__icon { width: 14px; height: 14px; flex: none; }
  .office {
    position: absolute;
    left: 40px;
    top: 232px;
    font-size: 16px;
    font-style: normal;
    line-height: 1.55;
  }
  .office__name { font-weight: 700; }
  .card--back .brand {
    position: absolute;
    right: 40px;
    top: 96px;
    display: flex;
    align-items: center;
    gap: 12px;
  }
  .card--back .brand__dot { width: 22px; height: 22px; }
  .card--back .brand__name {
    font-size: 20px;
    text-transform: none;
    letter-spacing: 0.02em;
    max-width: 190px;
    line-height: 1.25;
  }
</style>
</head>
<body>
<main class="sheet">

  <section class="card card--front" aria-label="Card front">
    <div class="brand">
      <div class="brand__mark">
        <span class="brand__dot"></span>
        <span class="brand__name">Meridian Lending Circle</span>
      </div>
      <span class="brand__web">www.meridian-lending.com</span>
    </div>
    <div class="card__band"></div>
  </section>

  <section class="card card--back" aria-label="Card back">
    <div class="person">
      <h1 class="person__name">Lena Hartwell</h1>
      <p class="person__role">Founder</p>
    </div>

    <ul class="contact">
      <li class="contact__item">
        <svg class="contact__icon" viewBox="0 0 14 14" aria-hidden="true">
          <rect x="3" y="1" width="8" height="12" rx="1.5" fill="none" stroke="var(--accent)" stroke-width="1.6"/>
          <line x1="5.5" y1="10.5" x2="8.5" y2="10.5" stroke="var(--accent)" stroke-width="1.4"/>
        </svg>
        <span>0841205577</span>
      </li>
      <li class="contact__item">
        <svg class="contact__icon" viewBox="0 0 14 14" aria-hidden="true">
          <rect x="1" y="3" width="12" height="8.5" rx="1" fill="none" stroke="var(--accent)" stroke-width="1.6"/>
          <polyline points="1.5,3.8 7,8 12.5,3.8" fill="none" stroke="var(--accent)" stroke-width="1.4"/>
        </svg>
        <span>lena@meridian-lending.com</span>
      </li>
    </ul>

    <address class="office">
      <div class="office__name">Meridian Lending Circle</div>
      <div>Suite 210, 14 Harbourview Ave. Eastpoint</div>
    </address>

    <div class="brand">
      <span class="brand__dot"></span>
      <span class="brand__name">Meridian Lending Circle</span>
    </div>

    <div class="card__band"></div>
  </section>

</main>
</body>
</html>
```